Kestrel Forge Tech
Bus. Cards/Stationary/Presentation
Kestrel Forge Tech - Information Technology
Creative Brief
Use specific fonts
Open to ideas on font pairing
Professional
Wendell Pask
Owner
218 Larkspur Avenue Suite 4400 Beaumont, TX 77701
Wendell.Pask@kestrelforgetech.com
www.kestrelforgetech.com
I am open to my logo displayed on the back. I am also open to ideas on the back of business card. Be creative on front and back.

```html
<!DOCTYPE html>
<html lang="en">
<head>
<meta charset="utf-8">
<title>Kestrel Forge Tech – Business Card</title>
<link rel="stylesheet" href="https://fonts.googleapis.com/css2?family=Open+Sans:wght@400;600;700&display=swap">
<style>
  :root {
    --card-bg: #ffffff;
    --page-bg: #ffffff;
    --ink: #3a3a3a;
    --brand-gray: #6d6e71;
    --brand-green: #7cc142;
    --faint-gray: #f3f3f3;
    --border: #c8c8c8;
  }
  html, body {
    margin: 0;
    padding: 0;
    width: 1200px;
    height: 689px;
    overflow: hidden;
    background: var(--page-bg);
  }
  .card {
    position: relative;
    width: 1200px;
    height: 689px;
    box-sizing: border-box;
    border: 2px solid var(--border);
    background: var(--card-bg);
    font-family: "Open Sans", Arial, sans-serif;
    color: var(--ink);
    overflow: hidden;
  }
  .backdrop-circle {
    position: absolute;
    left: 610px;
    top: 40px;
    width: 560px;
    height: 560px;
    border-radius: 50%;
    background: var(--faint-gray);
  }
  .brand-dot {
    position: absolute;
    left: 262px;
    top: 42px;
    width: 104px;
    height: 104px;
    border-radius: 50%;
    background: var(--brand-green);
  }
  .brand-name {
    position: absolute;
    left: 38px;
    top: 190px;
    margin: 0;
    font-size: 60px;
    font-weight: 700;
    letter-spacing: -1px;
    color: var(--brand-gray);
    line-height: 1;
    white-space: nowrap;
  }
  .person-name {
    position: absolute;
    left: 43px;
    top: 390px;
    margin: 0;
    font-size: 38px;
    font-weight: 600;
    color: var(--brand-green);
    line-height: 1;
  }
  .person-title {
    position: absolute;
    left: 43px;
    top: 437px;
    margin: 0;
    font-size: 31px;
    font-weight: 400;
    color: var(--ink);
    line-height: 1;
  }
  .contact {
    position: absolute;
    top: 545px;
    margin: 0;
    font-size: 22px;
    line-height: 38px;
    color: var(--ink);
    font-style: normal;
    white-space: nowrap;
  }
  .contact-address { left: 43px; }
  .contact-phones { left: 512px; top: 553px; }
  .contact .label { font-weight: 700; }
  .website {
    position: absolute;
    right: 26px;
    top: 619px;
    margin: 0;
    font-size: 24px;
    font-weight: 600;
    color: var(--brand-green);
    line-height: 1;
  }
</style>
</head>
<body>
  <main class="card">
    <div class="backdrop-circle" aria-hidden="true"></div>

    <div class="brand-dot" aria-hidden="true"></div>
    <h1 class="brand-name">Kestrel Forge Tech</h1>

    <h2 class="person-name">Wendell Pask</h2>
    <p class="person-title">Owner</p>

    <address class="contact contact-address">
      <span class="label">A:</span> 218 Larkspur Avenue<br>
      Suite 4400 Beaumont, TX 77701<br>
      <span class="label">E:</span> Wendell.Pask@kestrelforgetech.com
    </address>

    <p class="contact contact-phones">
      <span class="label">P:</span> 409.555.0147<br>
      <span class="label">C:</span> 409.555.0183<br>
      <span class="label">F:</span> 409.555.0192
    </p>

    <p class="website">www.kestrelforgetech.com</p>
  </main>
</body>
</html>
```